Health Coach needs a creative and catchy Chatnook Ad Image to increase page likes

I have just recently launched a health coaching business and would like to increase my Chatnook awareness and page likes.
I plan on doing a “page liking” campaign through Chatnook and want a creative, catchy and unique image to help make my campaign successful.
I want a versatile image, as I am aiming to run this campaign on Chatnook for a while (few months).
The image is to be 1200 x 444 pixels, with an image ratio of 8:3, and because it is going on Chatnook it cannot have any overlaid text (or very little).
So, the image will have to be very visually appealing and catchy!
I am happy for some creative illustrations and drawings to be used to help portray my message (please see attached for some sample pictures)
I would like the image to portray the following:
-health
-happiness
-change
Some of my key messages that you could include:
-holistic health
-health & wellness
-health, nutrition, lifestyle
-Food, fitness, happiness

In addition, a call to action that could be incorporated could be:
"i can help you"
..or something similar (but only if this can fit).

I have attached some images of myself to be used.

Target Market(s)

People looking for health and fitness advice

Industry/Entity Type

Health And Wellness

Colors

Requirements
Nice to have
• illustrations as per 2 sample images provided
• call to action if can fit

```html
<!DOCTYPE html>
<html lang="en">
<head>
<meta charset="utf-8">
<title>Health Happiness Change – I can help you</title>
<link rel="stylesheet" href="https://fonts.googleapis.com/css2?family=Tinos:ital,wght@1,700&display=swap">
<style>
  :root {
    --paper: #ffffff;
    --teal: #8adfd6;
    --lime: #e3f842;
    --curl: #f2f3f3;
    --curl-shadow: #e2e6e6;
    --headline: #ffffff;
    --cta: #1f3a12;
    --photo-leaf: #3d5a3a;
    --photo-sky: #8fb0c0;
    --photo-stone: #8e8a83;
    --ornament: rgba(255, 255, 255, 0.28);
  }
  html, body {
    margin: 0;
    padding: 0;
    overflow: hidden;
    background: var(--paper);
  }
  .canvas {
    position: relative;
    width: 1200px;
    height: 800px;
    overflow: hidden;
    background: var(--paper);
    font-family: "Tinos", "Times New Roman", serif;
  }
  .spray {
    position: absolute;
    left: 190px;
    top: 0;
    width: 150px;
    height: 300px;
    background: radial-gradient(ellipse at 80% 30%, rgba(138, 223, 214, 0.35), rgba(138, 223, 214, 0) 70%);
  }
  .panel {
    position: absolute;
    left: 325px;
    top: 0;
    width: 875px;
    height: 800px;
    background: var(--teal);
  }
  .stripe {
    position: absolute;
    left: 325px;
    width: 875px;
    background: var(--lime);
  }
  .stripe--health { top: 58px; height: 104px; }
  .stripe--happiness { top: 247px; height: 98px; }
  .stripe--change { top: 427px; height: 96px; }
  .portrait {
    position: absolute;
    left: 390px;
    top: 40px;
    width: 335px;
    height: 760px;
    background: linear-gradient(180deg, var(--photo-leaf) 0%, var(--photo-sky) 38%, var(--photo-leaf) 52%, var(--photo-stone) 66%, #6f6b65 100%);
  }
  .fruit {
    position: absolute;
    border-radius: 50%;
    background: var(--ornament);
  }
  .fruit--apple-top { left: 1055px; top: 115px; width: 95px; height: 85px; }
  .fruit--grapes-right { left: 1060px; top: 345px; width: 130px; height: 105px; }
  .fruit--grapes-left { left: 735px; top: 420px; width: 140px; height: 120px; }
  .fruit--apple-bottom { left: 730px; top: 595px; width: 120px; height: 105px; }
  .curl {
    position: absolute;
    left: 0;
    top: 0;
  }
  .word {
    position: absolute;
    margin: 0;
    color: var(--headline);
    font-style: italic;
    font-weight: 700;
    font-size: 66px;
    line-height: 1;
  }
  .word--health { left: 755px; top: 80px; }
  .word--happiness { left: 800px; top: 266px; }
  .word--change { left: 930px; top: 443px; }
  .cta {
    position: absolute;
    right: 20px;
    top: 732px;
    margin: 0;
    color: var(--cta);
    font-style: italic;
    font-weight: 700;
    font-size: 45px;
    line-height: 1;
  }
</style>
</head>
<body>
<main class="canvas">
  <div class="spray" role="img" aria-label="Soft teal spray texture"></div>
  <div class="panel"></div>
  <div class="stripe stripe--health"></div>
  <div class="stripe stripe--happiness"></div>
  <div class="stripe stripe--change"></div>

  <div class="portrait" role="img" aria-label="Photo of the health coach standing on outdoor stone stairs by a railing, trees behind"></div>

  <div class="fruit fruit--apple-top" role="img" aria-label="Line drawing of an apple and a strawberry"></div>
  <div class="fruit fruit--grapes-right" role="img" aria-label="Line drawing of grapes and a strawberry"></div>
  <div class="fruit fruit--grapes-left" role="img" aria-label="Line drawing of a bunch of grapes"></div>
  <div class="fruit fruit--apple-bottom" role="img" aria-label="Line drawing of an apple"></div>

  <svg class="curl" width="1200" height="800" viewBox="0 0 1200 800" aria-hidden="true">
    <path d="M728,800 Q880,720 990,590 Q1015,545 1030,548 Q1060,600 1110,612 Q1170,620 1200,580 L1200,800 Z" fill="var(--curl)"/>
    <path d="M728,800 Q880,720 990,590 Q1000,650 1040,800 Z" fill="var(--curl-shadow)" opacity="0.5"/>
  </svg>

  <h1 class="word word--health">Health</h1>
  <h2 class="word word--happiness">Happiness</h2>
  <h2 class="word word--change">Change</h2>

  <p class="cta">I can help you!</p>
</main>
</body>
</html>
```